Simple, Elegant, Clean Homepage Design For Jobrova.com - for job seekers.

Hello, we're going to start this site by posting a project for ONE page of it - the homepage. I've attached a simple wireframe I created and we'll be using logo #1 in the attached PDF.

Anyway, all the wireframe shows is where the elements should be. You'll put in placeholder image(s) where needed. (i.e. The BrightDesk banner.)

We are looking for a simple, clean site - very minimalistic but also one that grabs the eye.

Simple, clean menu across the top...the little links at the bottom...

And in the middle show us some headline styles, subhead styles, body copy font style, and bullets we can use.

As you can see there is also a search tool for employers in the upper right, so we'd like to see your vision of that as well.

Thanks!

Tom

P.S. You can just put in some garbled example text to illustrate fonts and other elements listed in the description.

P.P.S. I just added a new PDF to this project showing some updated tag lines we like with the "jobrova.com/your-name-here" thing we like. See if this can be integrated into your existing designs - or new designs.

Target Market(s)

Job Seekers

Number of Pages Required

1 page

Font styles to use
Sans Serif

Colors
ffffff
0456a4
000000
c5c5c5

Requirements
Must have
• Must be a simple, clean, optimized HTML/CSS design. We are looking for a minimalistic approach, so that we can easily highlight certain features/text/icons with color.
Nice to have
• White background, elegant and "soft" outlines for sections, easy to read font, headline fonts/colors that grab, tasteful bullets.
Should not have
• Complex design
• hard to read fonts
• busy/loud design
• not too serious, not too casual

```html
<!DOCTYPE html>
<html lang="en">
<head>
<meta charset="utf-8">
<title>Jobrova.com – Homepage</title>
<link href="https://fonts.googleapis.com/css2?family=Lato:ital,wght@0,300;0,400;0,700;0,900;1,400;1,700&display=swap" rel="stylesheet">
<style>
:root{
  --blue:#0456a4;
  --blue-light:#3fa0e6;
  --black:#000000;
  --white:#ffffff;
  --silver:#c5c5c5;
  --ink:#2b2b2b;
  --text:#6d6d6d;
  --dark:#424447;
  --darker:#333538;
  --band:#eceef0;
  --green:#7dc242;
  --green-dark:#5c9e2a;
  --orange:#f28a1e;
}
*{box-sizing:border-box;margin:0;padding:0}
html,body{width:1200px;height:2668px;overflow:hidden}
body{font-family:"Lato",Arial,sans-serif;background:var(--white);color:var(--ink);position:relative}
.abs{position:absolute}
.btn{display:inline-block;background:var(--blue);color:var(--white);font-weight:700;font-size:19px;padding:15px 34px;border-radius:3px;text-decoration:none}

/* hero */
.hero{left:0;top:0;width:1200px;height:500px}
.hero-photo{left:0;top:0;width:1200px;height:500px;background:linear-gradient(180deg,#e9eef2 0%,#cfd6dc 45%,#9aa3aa 100%)}
.brand{left:36px;top:32px;display:flex;align-items:center;gap:10px}
.brand-mark{width:26px;height:26px;border-radius:50%;background:var(--blue)}
.brand-name{font-size:40px;font-weight:700;color:var(--blue);letter-spacing:-.5px}
.brand-tag{left:72px;top:84px;font-size:12px;color:var(--text)}
.nav{left:330px;top:16px;display:flex;gap:58px;font-size:14px;font-weight:700;color:var(--ink);letter-spacing:.5px}
.nav-note{left:530px;top:44px;font-size:13px;color:var(--ink)}
.headline{left:370px;top:196px;width:480px;text-align:center}
.headline h1{font-style:italic;font-weight:400;font-size:38px;line-height:48px;color:var(--ink);white-space:nowrap}
.headline h1 span{color:var(--blue);text-decoration:underline;font-weight:700}
.headline p{margin:12px auto 0;width:400px;font-size:15px;color:var(--ink);line-height:21px}
.employers{left:872px;top:0;width:328px}
.employers-tab{background:var(--blue);color:var(--white);font-weight:700;font-size:22px;text-align:center;height:44px;line-height:44px;letter-spacing:1px}
.employers-search{background:var(--white);height:72px;padding:16px;display:flex;gap:8px}
.employers-search .field{flex:1;border:1px solid var(--silver);border-radius:3px;font-size:14px;color:#999;padding:10px}
.employers-search .go{width:44px;background:var(--blue);border-radius:3px}
.seminar{left:872px;top:124px;width:328px;height:352px;background:var(--green)}
.seminar h2{color:var(--white);font-size:44px;font-weight:900;text-align:center;margin-top:22px}
.seminar .sub{background:var(--green-dark);color:var(--white);text-align:center;font-size:18px;font-weight:700;height:30px;line-height:30px;margin:6px 20px 0}
.seminar-photo{margin:16px 20px 0;height:170px;background:linear-gradient(135deg,#e6e9ec,#b8c0c6)}
.seminar .register{margin:14px 20px 0;background:var(--green-dark);color:var(--white);text-align:center;font-weight:900;font-size:22px;height:48px;line-height:48px;letter-spacing:.5px}

/* help */
.help{left:0;top:500px;width:1200px;height:520px;background:var(--dark)}
.help-title{left:56px;top:46px;font-size:30px;font-weight:700;color:var(--blue-light);line-height:36px}
.help-lead{left:430px;top:40px;width:720px;font-size:23px;line-height:32px;font-weight:300;color:#bfc2c5}
.help-rule{left:56px;top:200px;width:1088px;height:1px;background:#5a5d61}
.help-col{top:232px;width:330px;text-align:center}
.help-col h3{color:var(--white);font-size:22px;font-weight:900;letter-spacing:.5px}
.help-col p{margin-top:18px;font-size:16px;line-height:24px;color:#b4b7ba;text-align:justify}

/* companies */
.section-bar{left:0;width:1200px;height:64px;background:var(--band);border-top:1px solid #dde0e3;border-bottom:1px solid #dde0e3}
.section-bar h2{position:absolute;left:56px;top:16px;font-size:28px;font-weight:700;color:var(--ink)}
.companies-photo{left:56px;top:1130px;width:630px;height:270px;background:linear-gradient(135deg,#dfe5ea,#9aa7b1)}
.company{left:720px;top:1130px;width:424px}
.company-mark{display:flex;align-items:center;gap:10px;height:60px}
.company-mark i{width:22px;height:22px;background:var(--blue);display:block}
.company-mark b{font-size:22px;color:var(--ink)}
.company h3{margin-top:10px;font-size:28px;font-weight:700;color:var(--ink)}
.company p{margin-top:10px;font-size:16px;line-height:24px;color:var(--text)}
.company .btn{margin-top:18px}

/* advertise */
.advertise{left:56px;top:1470px;width:370px}
.advertise h2{font-size:36px;line-height:44px;font-weight:900;color:var(--ink)}
.advertise p{margin-top:24px;font-size:16px;line-height:24px;color:var(--text)}
.advertise .btn{margin-top:30px}
.dashboard{left:460px;top:1470px;width:700px;height:400px;border:1px solid var(--silver);background:#f7f8f9}

/* news */
.news-col{top:2010px;width:340px}
.news-photo{height:190px;background:linear-gradient(135deg,#5b6670,#1f2a33)}
.news-col h3{margin-top:26px;font-size:27px;line-height:33px;font-weight:900;color:var(--ink)}
.news-col p{margin-top:16px;font-size:16px;line-height:24px;color:var(--text)}
.news-col .btn{position:absolute;top:476px;left:0}

/* footer */
.footer{left:0;top:2560px;width:1200px;height:108px;background:var(--darker);color:var(--white)}
.footer .copy{position:absolute;left:56px;top:76px;font-size:12px;color:#aaa}
.footer-links{position:absolute;right:56px;top:26px;display:grid;grid-template-columns:auto auto auto;column-gap:50px;row-gap:12px;font-size:17px;font-weight:700;text-align:right}
</style>
</head>
<body>

<header class="abs hero">
  <div class="abs hero-photo" role="img" aria-label="Photo of a businessman looking through a telescope above the clouds"></div>
  <div class="abs brand"><span class="brand-mark"></span><span class="brand-name">jobrova</span></div>
  <div class="abs brand-tag">Your career, one link away</div>
  <nav class="abs nav"><span>ABOUT</span><span>SUPPORT</span><span>SIGN IN</span><span>FREE TRAINING</span></nav>
  <div class="abs nav-note">jobrova.com/your-name-here</div>
  <div class="abs headline">
    <h1>One Amazing <span>Link</span><br>for the Rest of Your Career.</h1>
    <p>Lorem ipsum dolor sit amet, consectetur adipiscing elit. Mauris ultricies molestie orci.</p>
  </div>
  <div class="abs employers">
    <div class="employers-tab">EMPLOYERS</div>
    <div class="employers-search"><div class="field">Search candidates…</div><div class="go"></div></div>
  </div>
  <aside class="abs seminar">
    <h2>BrightDesk</h2>
    <div class="sub">Online Seminar</div>
    <div class="seminar-photo" role="img" aria-label="Photo of a smiling presenter with a headset"></div>
    <div class="register">REGISTER HERE</div>
  </aside>
</header>

<section class="abs help">
  <h2 class="abs help-title">How we can<br>help you</h2>
  <p class="abs help-lead">Fusce placerat risus sit amet lectus egestas, pretium porttitor nisi facilisis. Morbi pellentesque odio et nulla interdum viverra. Nam suscipit, eros ut vulputate ultrices, libero odio mollis justo, nec varius felis odio ut nisi.</p>
  <div class="abs help-rule"></div>
  <div class="abs help-col" style="left:56px"><h3>FIND A JOB</h3><p>Sed felis nisl, congue at finibus in, porttitor ut elit. Etiam et mattis ipsum. Praesent vel molestie mi. Duis in nunc nunc. Class aptent taciti sociosqu ad litora torquent per conubia nostra, per inceptos himenaeos.</p></div>
  <div class="abs help-col" style="left:435px"><h3>YOUR RESUME</h3><p>Sed felis nisl, congue at finibus in, porttitor ut elit. Etiam et mattis ipsum. Praesent vel molestie mi. Duis in nunc nunc. Class aptent taciti sociosqu ad litora torquent per conubia nostra, per inceptos himenaeos.</p></div>
  <div class="abs help-col" style="left:814px"><h3>TRAIN YOURSELF</h3><p>Sed felis nisl, congue at finibus in, porttitor ut elit. Etiam et mattis ipsum. Praesent vel molestie mi. Duis in nunc nunc. Class aptent taciti sociosqu ad litora torquent per conubia nostra, per inceptos himenaeos.</p></div>
</section>

<div class="abs section-bar" style="top:1040px"><h2>Companies Hiring Now</h2></div>
<div class="abs companies-photo" role="img" aria-label="Photo of a team meeting around a presentation board"></div>
<div class="abs company">
  <div class="company-mark"><i></i><b>Northline Studio</b></div>
  <h3>Northline Studio</h3>
  <p>Sed felis nisl, congue at finibus in, porttitor ut elit. Etiam et mattis ipsum. Praesent vel molestie mi. Duis in nunc nunc. Class aptent taciti sociosqu ad litora torquent per conubia nostra, per inceptos himenaeos.</p>
  <a class="btn">Learn More</a>
</div>

<div class="abs advertise">
  <h2>Advertise Your Jobs.<br>Hire the right people.</h2>
  <p>Sed felis nisl, congue at finibus in, porttitor ut elit. Etiam et mattis ipsum. Praesent vel molestie mi. Duis in nunc nunc. Class aptent taciti sociosqu ad litora torquent per conubia nostra, per inceptos himenaeos.</p>
  <a class="btn">Get an Employer Account</a>
</div>
<svg class="abs dashboard" viewBox="0 0 700 400" aria-label="Employer dashboard with statistics">
  <rect x="0" y="0" width="700" height="36" fill="#ffffff"/>
  <text x="16" y="24" font-family="Lato,sans-serif" font-size="14" font-weight="700" fill="#2b2b2b">My Dashboard</text>
  <rect x="16" y="50" width="200" height="120" fill="#fff" stroke="#e0e0e0"/>
  <text x="30" y="72" font-family="Lato,sans-serif" font-size="11" fill="#888">Profile views</text>
  <text x="60" y="130" font-family="Lato,sans-serif" font-size="44" font-weight="700" fill="#f28a1e">43K</text>
  <rect x="230" y="50" width="220" height="120" fill="#fff" stroke="#e0e0e0"/>
  <text x="244" y="72" font-family="Lato,sans-serif" font-size="11" fill="#888">Applications</text>
  <polyline points="244,150 280,130 316,138 352,108 388,118 436,92" fill="none" stroke="#0456a4" stroke-width="2"/>
  <rect x="464" y="50" width="220" height="120" fill="#fff" stroke="#e0e0e0"/>
  <text x="478" y="72" font-family="Lato,sans-serif" font-size="11" fill="#888">Open positions</text>
  <text x="478" y="130" font-family="Lato,sans-serif" font-size="34" font-weight="700" fill="#2b2b2b">32</text>
  <rect x="16" y="184" width="330" height="200" fill="#fff" stroke="#e0e0e0"/>
  <text x="30" y="206" font-family="Lato,sans-serif" font-size="11" fill="#888">Weekly activity</text>
  <g fill="#3fa0e6">
    <rect x="40" y="300" width="22" height="70"/><rect x="76" y="270" width="22" height="100"/><rect x="112" y="320" width="22" height="50"/><rect x="148" y="250" width="22" height="120"/><rect x="184" y="290" width="22" height="80"/><rect x="220" y="240" width="22" height="130"/><rect x="256" y="280" width="22" height="90"/><rect x="292" y="310" width="22" height="60"/>
  </g>
  <rect x="360" y="184" width="324" height="200" fill="#fff" stroke="#e0e0e0"/>
  <text x="374" y="206" font-family="Lato,sans-serif" font-size="11" fill="#888">Top sources</text>
  <g fill="#0456a4">
    <rect x="374" y="228" width="240" height="14"/><rect x="374" y="258" width="190" height="14"/><rect x="374" y="288" width="150" height="14"/><rect x="374" y="318" width="100" height="14"/><rect x="374" y="348" width="60" height="14"/>
  </g>
</svg>

<div class="abs section-bar" style="top:1920px"><h2>What's new at Jobrova</h2></div>
<article class="abs news-col" style="left:56px">
  <div class="news-photo" role="img" aria-label="Photo of hands counting money"></div>
  <h3>How much is your job worth right now?</h3>
  <p>Pellentesque sit amet tristique elit. Aliquam semper ultricies nulla nec molestie. Nulla facilisis. Cum sociis natoque penatibus.</p>
  <a class="btn">Calculate</a>
</article>
<article class="abs news-col" style="left:430px">
  <div class="news-photo" role="img" aria-label="Photo of a handshake at a job interview"></div>
  <h3>Who are the top companies hiring employees?</h3>
  <p>Ut tincidunt sit amet mauris eu tempor. Curabitur ornare vitae sem nec tempus. Nullam laoreet metus neque, eu hendrerit magna interdum a.</p>
  <a class="btn">Learn More</a>
</article>
<article class="abs news-col" style="left:804px">
  <div class="news-photo" role="img" aria-label="Photo of a person writing at a desk"></div>
  <h3>Are you ready for that job interview?</h3>
  <p>Aliquam erat volutpat. Nam auctor ut augue eu varius. Cras elementum accumsan pellentesque. Mauris nec nisi at ante faucibus consectetur.</p>
  <a class="btn">Take the test</a>
</article>

<footer class="abs footer">
  <div class="copy">Copyright 2017 Jobrova.com · ALL RIGHTS RESERVED</div>
  <div class="footer-links">
    <span>CONTACT US</span><span>TERMS &amp; CONDITIONS</span><span>DISCLAIMER</span>
    <span>PRIVACY</span><span>SIGN-IN</span><span>DIRECTORY</span>
  </div>
</footer>

</body>
</html>
```